Gutschein-Design zur Pflegeberatung
Zielgruppe
Wir feiern mit unserem Pflegedienst das 10 Jährige Jubiläum. Da es wegen der Corona Pandemie keine Feierlichkeiten geben kann, würde ich wir einen Gutschein für eine kostenlose Pflegeberatung erstellen lassen. Auf die Vorderseite bitte den Gutschein mit dem Text:
Bilder bitte aus den öffentlichen Portalen verwenden.
Gutschein zur Pflegeberatung
Wir unterstützen bei der Beantragung eines Pflegegrades und helfen bei abgelehnten Anträgen.
Gerne informieren wir Sie über umfangreiche Möglichkeiten der ambulante Pflege und erstellen einen individuellen Versorgungsplan. Darüber hinaus erhalte Sie praktische Tipps zu Alltagshilfen und konkrete Hilfestellungen rund um die Pflege, damit Sie noch so lange wie möglich zu
Hause bleiben können.
Unten bitte einfügen: Gutschein gültig bis einschließlich Juli 2022
Auf die Rückseite bitte eine kurze Info zu unserem 10 Jährigen bestehen.
Vielleicht vielleicht wieder mit dem Slogan, Seit 10 Jahren rund um die Uhr für Sie im Einsatz.
Aufgabenstellung
Da wir zwei ambulante Filialen betreiben, muss das Logo auf die zweite Filiale angepasst werden.
Der Text und die Informationen bleiben jedoch gleich. Der Gutschein sollte sofort auffallen und animieren, im Pflegedienst anzurufen.

```html
<!DOCTYPE html>
<html lang="en">
<head>
<meta charset="utf-8">
<title>Anniversary Care Voucher</title>
<link rel="stylesheet" href="https://fonts.googleapis.com/css2?family=Montserrat:ital,wght@0,500;0,600;0,700;0,800;1,700;1,800&family=Poppins:wght@600;700;800&display=swap">
<style>
  :root {
    --brand-blue: #4b55e6;
    --brand-blue-deep: #3a43c9;
    --ribbon-shadow: #2b329e;
    --panel-blue: #5a5ef0;
    --ribbon-cyan: #92e6f7;
    --ink: #111318;
    --navy: #1d2450;
    --paper: #ffffff;
    --room-light: #eef1f4;
    --room-mid: #c9d3dc;
    --room-deep: #8ea4b6;
    --screen-teal: #5fa9b9;
  }
  * { box-sizing: border-box; margin: 0; padding: 0; }
  html, body {
    width: 1200px; height: 450px; overflow: hidden;
    background: var(--paper);
    font-family: "Montserrat", sans-serif;
  }
  .voucher {
    position: relative; width: 1200px; height: 450px; overflow: hidden;
    background: var(--paper);
  }
  .edge-stripes {
    position: absolute; left: 200px; width: 1000px; height: 25px;
    background: repeating-linear-gradient(90deg, var(--brand-blue) 0 14px, var(--paper) 14px 24px);
  }
  .edge-stripes.top { top: 0; }
  .edge-stripes.bottom { bottom: 0; }
  .stub-shape { position: absolute; left: 0; top: 0; }
  .voucher-body {
    position: absolute; left: 0; top: 25px; width: 1200px; height: 400px;
  }
  .stub-column {
    position: absolute; left: 172px; top: 0; width: 36px; height: 400px;
    display: flex; align-items: center; justify-content: center;
  }
  .stub-note {
    transform: rotate(-90deg);
    white-space: nowrap;
    color: var(--paper);
    font-size: 10px; font-weight: 500; letter-spacing: 2.4px;
  }
  .photo-area {
    position: absolute; left: 208px; top: 0; width: 740px; height: 400px;
    overflow: hidden;
    background:
      radial-gradient(ellipse 120px 150px at 470px 210px, #d9c9bd 0%, rgba(217,201,189,0) 70%),
      radial-gradient(ellipse 110px 70px at 560px 150px, var(--screen-teal) 0%, rgba(95,169,185,0) 75%),
      radial-gradient(ellipse 110px 220px at 680px 260px, #6d8aa3 0%, rgba(109,138,163,0) 75%),
      linear-gradient(100deg, var(--room-light) 0%, #dfe5eb 40%, var(--room-mid) 70%, var(--room-deep) 100%);
  }
  .photo-wash {
    position: absolute; inset: 0;
    background: linear-gradient(90deg, rgba(255,255,255,0.72) 0%, rgba(255,255,255,0.45) 55%, rgba(255,255,255,0.15) 100%);
  }
  .anniversary-mark {
    position: absolute; left: 20px; top: 30px; width: 380px; height: 240px;
  }
  .arc-heading {
    font-family: "Poppins", sans-serif; font-weight: 700;
    font-size: 19px; letter-spacing: 2px; fill: var(--ink);
  }
  .big-number {
    position: absolute; left: 104px; top: 50px;
    font-family: "Poppins", sans-serif; font-weight: 800;
    font-size: 160px; line-height: 1; letter-spacing: -6px;
    color: var(--ink);
  }
  .ribbon { position: absolute; left: 66px; top: 232px; }
  .ribbon-label {
    font-family: "Montserrat", sans-serif; font-weight: 800;
    font-size: 20px; letter-spacing: 3px; fill: var(--navy);
  }
  .validity {
    position: absolute; left: 0; width: 740px; top: 352px;
    text-align: center;
    font-style: italic; font-weight: 800;
    font-size: 15px; letter-spacing: 3.4px;
    color: var(--navy);
  }
  .offer-panel {
    position: absolute; left: 948px; top: 0; width: 220px; height: 400px;
    background: var(--panel-blue);
  }
  .offer-title {
    position: absolute; top: 27px; left: 0; width: 220px; text-align: center;
    color: var(--paper); font-weight: 600; font-size: 11px; letter-spacing: 1.6px;
  }
  .offer-phone {
    position: absolute; top: 44px; left: 0; width: 220px; text-align: center;
    color: var(--paper); font-weight: 700; font-size: 18px; letter-spacing: 2px;
  }
  .staff-illustration {
    position: absolute; left: 28px; top: 110px; width: 170px; height: 270px;
    background:
      radial-gradient(ellipse 40px 120px at 35px 150px, rgba(86,200,210,0.75) 0%, rgba(86,200,210,0) 80%),
      radial-gradient(ellipse 40px 120px at 88px 150px, rgba(255,255,255,0.6) 0%, rgba(255,255,255,0) 80%),
      radial-gradient(ellipse 40px 120px at 140px 150px, rgba(86,200,210,0.75) 0%, rgba(86,200,210,0) 80%),
      linear-gradient(180deg, rgba(255,255,255,0.08), rgba(40,60,120,0.25));
  }
  .panel-trim {
    position: absolute; left: 1168px; top: 0; width: 32px; height: 400px;
    background: repeating-linear-gradient(90deg, var(--paper) 0 8px, var(--brand-blue) 8px 18px);
  }
</style>
</head>
<body>
<main class="voucher">
  <div class="edge-stripes top"></div>
  <div class="edge-stripes bottom"></div>

  <svg class="stub-shape" width="210" height="450" viewBox="0 0 210 450" aria-hidden="true">
    <path d="M 40 0 H 210 V 450 H 40 A 40 40 0 0 0 0 410 V 40 A 40 40 0 0 0 40 0 Z" fill="var(--brand-blue)"/>
  </svg>

  <section class="voucher-body">
    <div class="stub-column">
      <p class="stub-note">PLEASE USE PICTURES FROM THE PUBLIC PORTALS</p>
    </div>

    <div class="photo-area" role="img" aria-label="Photo of a nurse talking with a senior woman in a bright clinic room">
      <div class="photo-wash"></div>

      <div class="anniversary-mark">
        <svg width="380" height="120" viewBox="0 0 380 120">
          <defs>
            <path id="heading-arc" d="M 60 115 A 130 95 0 0 1 320 115"/>
          </defs>
          <text class="arc-heading" text-anchor="middle">
            <textPath href="#heading-arc" startOffset="50%">WORKING FOR YOU AROUND</textPath>
          </text>
        </svg>
        <div class="big-number">10</div>
      </div>

      <svg class="ribbon" width="300" height="62" viewBox="0 0 300 62">
        <polygon points="0,14 32,14 32,58 0,58 11,36" fill="var(--brand-blue-deep)"/>
        <polygon points="300,14 268,14 268,58 300,58 289,36" fill="var(--brand-blue-deep)"/>
        <polygon points="22,50 32,58 32,50" fill="var(--ribbon-shadow)"/>
        <polygon points="278,50 268,58 268,50" fill="var(--ribbon-shadow)"/>
        <rect x="22" y="4" width="256" height="46" fill="var(--ribbon-cyan)"/>
        <text class="ribbon-label" x="150" y="34" text-anchor="middle">ANNIVERSARY</text>
      </svg>

      <p class="validity">VOUCHER VALID UP TO AND INCLUDING JULY 2022</p>
    </div>

    <aside class="offer-panel">
      <p class="offer-title">FREE CARE CONSULTATION</p>
      <p class="offer-phone">1800-0000-7272</p>
      <div class="staff-illustration" role="img" aria-label="Illustration of three care staff members in medical uniforms"></div>
    </aside>

    <div class="panel-trim"></div>
  </section>
</main>
</body>
</html>
```